Coral Ride & Expedition St. Lucia

I want a website design that is vibrant, engaging, and converts.
I plan on using Squarespace for hosting.

Target Market(s)

Tourists and visitors to St. Lucia; Focus: North American Market then European

Industry/Entity Type

Travel & Tourism

Coding

Coded - Design and coding required

Number of Pages Required

1 page

```html
<!DOCTYPE html>
<html lang="en">
<head>
<meta charset="utf-8">
<title>Coral Ride &amp; Expedition St. Lucia</title>
<link rel="stylesheet" href="https://fonts.googleapis.com/css2?family=Poppins:ital,wght@0,300;0,400;0,500;0,600;0,700;1,400&display=swap">
<style>
:root{
  --cream:#faf0df;
  --ink:#0d0d0d;
  --white:#ffffff;
  --muted:#333333;
  --grey:#8a8a8a;
  --pill:#ece3d8;
  --line:#9a9a9a;
}
*{margin:0;padding:0;box-sizing:border-box}
html,body{width:1200px;height:4545px;overflow:hidden}
body{position:relative;background:var(--white);font-family:"Poppins",sans-serif;color:var(--ink)}
.abs{position:absolute}
.backdrop{position:absolute;left:0;top:0;width:1200px;height:4545px;pointer-events:none}
.photo{position:absolute}

.hero-photo{left:0;top:0;width:1200px;height:620px;background:linear-gradient(180deg,#a9aab0 0%,#c9c0b4 35%,#e6d6bb 55%,#b39a7c 75%,#8f7a62 100%)}
.brand{left:127px;top:47px;display:flex;align-items:center;gap:9px;color:var(--white);font-weight:500;font-size:14px;line-height:18px;white-space:nowrap}
.brand-dot{width:12px;height:12px;border-radius:50%;background:var(--white)}
.nav a{color:var(--white);font-size:14px;font-weight:500;text-decoration:none;position:absolute;white-space:nowrap}
.nav{left:425px;top:48px}
.nav-cta{left:935px;top:35px;width:136px;height:46px;border-radius:23px;background:var(--pill);color:var(--ink);font-size:14px;font-weight:500;display:flex;align-items:center;justify-content:center}
.hero-title{left:127px;top:205px;color:var(--white);font-weight:600;font-size:37px;line-height:42px}
.hero-link{left:129px;top:310px;color:var(--white);font-size:14px;font-weight:600;text-decoration:underline}

.feature-title{font-weight:500;font-size:33px;line-height:40px;width:470px}
.feature-text{font-size:15px;line-height:23px;color:var(--muted);width:445px}
.btn-dark{height:48px;border-radius:24px;background:var(--ink);color:var(--white);font-size:15px;font-weight:500;display:flex;align-items:center;justify-content:center;width:139px}

.quote-icon{left:555px;top:2140px;width:90px;height:66px}
.quote-text{left:0;width:1200px;top:2218px;text-align:center;font-style:italic;font-size:25px;line-height:36px;color:#222}
.quote-author{left:0;width:1200px;top:2355px;text-align:center;font-size:24px;font-weight:600}

.band-photo{left:0;top:2462px;width:1200px;height:560px;background:linear-gradient(180deg,#5a5044 0%,#6f6452 40%,#7b6d52 70%,#5e5240 100%)}
.band-title{left:0;width:1200px;top:2536px;text-align:center;color:var(--white);font-weight:500;font-size:33px;line-height:41px}

.section-title{left:0;width:1200px;text-align:center;font-weight:500;font-size:42px;line-height:50px}
.section-text{left:0;width:1200px;text-align:center;font-size:15px;line-height:23px;color:var(--muted)}
.tile{top:3262px;width:298px;height:363px}

.contact-photo{left:0;top:3618px;width:1200px;height:556px;background:radial-gradient(ellipse at 50% 60%,#efe0c6 0%,#f6ead6 45%,var(--cream) 80%)}
.field{top:4029px;height:52px;border:1px solid var(--line);background:var(--white);font-size:15px;padding:0 14px;display:flex;align-items:center;color:#222}
.submit{top:4029px;left:912px;width:126px;height:52px;background:var(--ink);color:var(--white);font-weight:600;font-size:16px;display:flex;align-items:center;justify-content:center}

.footer{left:0;top:4174px;width:1200px;height:371px;background:var(--ink);color:var(--white)}
.foot-head{position:absolute;top:60px;font-size:16px;font-weight:700;text-transform:uppercase}
.foot-body{position:absolute;top:96px;font-size:14px;line-height:19px}
.foot-list{position:absolute;top:95px;list-style:none;font-size:14px;line-height:30px}
.rights{position:absolute;top:303px;left:0;width:1200px;text-align:center;font-size:13px}
</style>
</head>
<body>

<div class="photo hero-photo" role="img" aria-label="Photo of a traveller sitting on an open-top car at a beach at sunset"></div>

<svg class="backdrop" viewBox="0 0 1200 4545" aria-hidden="true">
  <path d="M0,494 Q540,742 1200,494 L1200,1844 Q600,2200 0,1853 Z" fill="#faf0df"/>
</svg>

<div class="abs brand"><span class="brand-dot"></span>Coral Ride &amp; Expedition St. Lucia</div>
<nav class="abs nav">
  <a style="left:0">Home</a>
  <a style="left:79px">Adventure</a>
  <a style="left:189px">About Us</a>
  <a style="left:288px">Coral Ride</a>
  <a style="left:410px">Contact</a>
</nav>
<div class="abs nav-cta">Get Started</div>

<h1 class="abs hero-title">Find your happiness<br>and learn to put it first.</h1>
<a class="abs hero-link">Get Started</a>

<div class="photo" style="left:127px;top:732px;width:440px;height:486px;background:linear-gradient(180deg,#8fb6d6 0%,#b9cfdf 45%,#c77a44 70%,#dcd6cf 100%)" role="img" aria-label="Photo of a smiling woman in sunglasses leaning on a white jeep"></div>
<h2 class="abs feature-title" style="left:618px;top:800px">Lorem ipsum dolor sit ame conselorec tetur adipiscin incididunt ut labore et</h2>
<p class="abs feature-text" style="left:618px;top:942px">Lorem ipsum dolor sit amet, consectetur adipiscing elit, sed do eiusmod tempor incididunt ut labore et dolore magna aliqua. Quis ipsum suspendisse ultrices gravid isus comm odo viverra maecenas accumsan lacus vel facilisis.</p>
<div class="abs btn-dark" style="left:618px;top:1094px">Get Started</div>

<h2 class="abs feature-title" style="left:131px;top:1377px">Lorem ipsum dolor sit ame conselorec tetur adipiscin incididunt ut labore et</h2>
<p class="abs feature-text" style="left:131px;top:1519px">Lorem ipsum dolor sit amet, consectetur adipiscing elit, sed do eiusmod tempor incididunt ut labore et dolore magna aliqua. Quis ipsum suspendisse ultrices gravid isus comm odo viverra maecenas accumsan lacus vel facilisis.</p>
<div class="abs btn-dark" style="left:131px;top:1671px">Get Started</div>
<div class="photo" style="left:632px;top:1308px;width:438px;height:487px;background:linear-gradient(160deg,#8d7450 0%,#d9b46a 35%,#c8cdd2 60%,#7e8891 100%)" role="img" aria-label="Photo of a woman and child looking out of a car window on a sunny coast road"></div>

<svg class="abs quote-icon" viewBox="0 0 90 66" aria-hidden="true">
  <g fill="none" stroke="#8a8a8a" stroke-width="5">
    <circle cx="20" cy="19" r="15"/>
    <path d="M35,19 C35,42 24,56 6,62"/>
    <circle cx="66" cy="19" r="15"/>
    <path d="M81,19 C81,42 70,56 52,62"/>
  </g>
</svg>
<p class="abs quote-text">Lorem ipsum dolor sit amet, consectetur adipiscing elit,<br>sed do eiusmod tempor incididunt ut labore et dolore<br>magna aliqua. Quis ipsum suspendisse gravida</p>
<p class="abs quote-author">—Mara L.</p>

<div class="photo band-photo" role="img" aria-label="Photo of a couple with their dog sitting at the back of a pickup truck in a forest"></div>
<svg class="backdrop" viewBox="0 0 1200 4545" aria-hidden="true">
  <path d="M0,2895 Q600,3140 1200,2877 L1200,3030 L0,3030 Z" fill="#ffffff"/>
</svg>
<h2 class="abs band-title">Lorem ipsum dolor sit ame conselorec<br>tetur adipiscin incididunt ut labor<br>nas accumsan lacucilisis.</h2>

<h2 class="abs section-title" style="top:3112px">Adventures</h2>
<p class="abs section-text" style="top:3185px">Lorem ipsum dolor sit amet, consectetur adipiscing elit, sed do<br>eiusmod tempor incididunt ut labore et dolore magna.</p>
<div class="photo tile" style="left:127px;background:linear-gradient(180deg,#c9cfd3 0%,#a8a89a 45%,#6e6a48 100%)" role="img" aria-label="Photo of three friends sitting on the back of a car in a field"></div>
<div class="photo tile" style="left:450px;background:linear-gradient(180deg,#7fb3e0 0%,#a9cbe6 40%,#3d4a55 70%,#6e8fa8 100%)" role="img" aria-label="Photo of a woman in a sun hat stretching beside a car by the sea"></div>
<div class="photo tile" style="left:773px;background:linear-gradient(180deg,#c8c2b6 0%,#b8675a 40%,#d9d2c4 70%,#5b5650 100%)" role="img" aria-label="Photo of a family sitting in the open boot of a car"></div>

<div class="photo contact-photo" role="img" aria-label="Faint photo of a traveller beside a car"></div>
<svg class="backdrop" viewBox="0 0 1200 4545" aria-hidden="true">
  <path d="M0,3610 L1200,3610 L1200,3636 Q600,3955 0,3636 Z" fill="#ffffff"/>
</svg>
<h2 class="abs section-title" style="top:3880px">Contact Us</h2>
<p class="abs section-text" style="top:3953px">Lorem ipsum dolor sit amet, consectetur adipiscing elit, sed do<br>eiusmod tempor incididunt ut labore et dolore magna.</p>
<div class="abs field" style="left:162px;width:241px">Name:</div>
<div class="abs field" style="left:413px;width:241px">Email:</div>
<div class="abs field" style="left:664px;width:241px">Phone:</div>
<div class="abs submit">Submit</div>

<footer class="abs footer">
  <h3 class="foot-head" style="left:127px">About Us</h3>
  <p class="foot-body" style="left:127px;width:360px">Lorem ipsum dolor sit amet, cons ectetur adipiscing elit, sed do loree iusmod tempor incididunt ut labore et dolore magna aliquis ipsum suspendisse ultrices gra et dolore magna aliquis ipsum suspend.</p>
  <h3 class="foot-head" style="left:591px">Links</h3>
  <ul class="foot-list" style="left:593px">
    <li>Home</li><li>Adventure</li><li>About Us</li><li>Coral Ride</li><li>Contact</li>
  </ul>
  <h3 class="foot-head" style="left:824px">Adventures</h3>
  <ul class="foot-list" style="left:824px">
    <li>Lorem ipsum dolor sit</li><li>amet, consectetur</li><li>adipiscing elit, sed do</li><li>eiusmod tempor</li><li>incididunt ut lab.</li>
  </ul>
  <p class="rights">All Rights are reserved.</p>
</footer>

</body>
</html>
```